"BREAKING NEWS!" Fitness photos needed

Hello.... We are creating our new ads for Chatterloop and Glimmerpost and we need some photos manipulated and text added.

We have 5 photos total that we would like to have the Headline read "Breaking News" and we'll be split testing two different quotes, so I'd like to have:

AD #1:
Breaking News - Finally! Brackenford Gets the Gym That Actually Delivers Results (and It's Fun!)

And then a second set on the same photos that read:

AD #2:
Breaking News - Brackenford Residents Ditch Boring Workouts for This Life-Changing Fitness Experience

I'd like the photos to pop and stand out, so if color corrections need to be done, please feel free.

I've attached all photos and an example photo that DOES NOT need to be the same. It's just an example I saw that caught my eye, but I feel could be done better.

Thank you!

```html
<!DOCTYPE html>
<html lang="en">
<head>
<meta charset="utf-8">
<title>Breaking News – Gym Ads</title>
<link href="https://fonts.googleapis.com/css2?family=Bebas+Neue&family=Montserrat:ital,wght@0,300;0,400;0,600;0,700;0,800;1,900&display=swap" rel="stylesheet">
<style>
  :root {
    --page: #ffffff;
    --navy: #0b1020;
    --yellow: #ffd100;
    --white: #ffffff;
    --red-a: #ff2a2a;
    --red-b: #b0001a;
    --blue-a: #2d6bff;
    --blue-b: #0a2a9c;
    --silver-a: #ffffff;
    --silver-b: #9aa0aa;
    --photo-a: #c9b27a;
    --photo-b: #5a4a5e;
    --photo-c: #2a2236;
  }
  * { box-sizing: border-box; margin: 0; padding: 0; }
  html, body {
    width: 783px; height: 1200px; overflow: hidden;
    background: var(--page);
    font-family: "Montserrat", sans-serif;
  }
  .canvas { position: relative; width: 783px; height: 1200px; }

  .ad { position: absolute; background: var(--navy); overflow: hidden; color: var(--white); }
  .ad--square { left: 190px; top: 168px; width: 438px; height: 438px; }
  .ad--wide { left: 64px; top: 684px; width: 690px; height: 361px; }

  .ad__art { position: absolute; inset: 0; width: 100%; height: 100%; }

  .ad > * { position: absolute; }

  .offer-badge {
    background: var(--yellow); color: var(--navy);
    display: flex; flex-direction: column; align-items: center; justify-content: center;
    line-height: 0.95; text-align: center;
  }
  .offer-badge__small { font-weight: 400; }
  .offer-badge__big { font-weight: 800; letter-spacing: -0.02em; }

  .live-tag {
    background: linear-gradient(90deg, #ffe34d, var(--yellow));
    color: var(--navy); font-weight: 900; font-style: italic;
    display: flex; align-items: center; justify-content: center; gap: 3px;
    transform: skewX(-14deg);
  }
  .live-tag__dot { width: 0.45em; height: 0.45em; border-radius: 50%; background: var(--navy); }

  .mark-x { color: var(--yellow); font-weight: 800; line-height: 1; }

  .news-band {
    display: flex; align-items: center; padding-left: 0.35em;
    transform: skewX(-14deg);
  }
  .news-band--red {
    background: linear-gradient(180deg, var(--red-a), var(--red-b));
    box-shadow: -60px 0 18px -14px rgba(255,40,40,0.55);
  }
  .news-band--blue {
    background: linear-gradient(180deg, var(--blue-a), var(--blue-b));
    box-shadow: 40px 0 16px -14px rgba(60,120,255,0.5);
  }
  .news-band__word {
    font-weight: 900; font-style: italic; letter-spacing: -0.02em; line-height: 1;
    background: linear-gradient(180deg, var(--silver-a) 40%, var(--silver-b));
    -webkit-background-clip: text; background-clip: text; color: transparent;
    transform: skewX(4deg);
  }

  .headline-finally { font-family: "Bebas Neue", sans-serif; line-height: 1; color: var(--white); }
  .subhead { font-weight: 400; line-height: 1.22; color: var(--white); white-space: nowrap; }
  .aside-fun { font-family: "Bebas Neue", sans-serif; line-height: 1; color: var(--white); white-space: nowrap; }

  .cta {
    background: var(--yellow); color: var(--navy); font-weight: 700;
    display: flex; align-items: center; justify-content: center; letter-spacing: 0.01em;
  }
  .site-url { font-weight: 600; font-size: 11px; color: var(--white); }

  .dot-grid { display: grid; grid-template-columns: repeat(3, 3px); gap: 4px; }
  .dot-grid span { width: 3px; height: 3px; border-radius: 50%; background: #8a90a0; }

  /* square ad placement */
  .ad--square .offer-badge { left: 31px; top: 91px; width: 101px; height: 79px; border-radius: 9px; }
  .ad--square .offer-badge__small { font-size: 17px; }
  .ad--square .offer-badge__big { font-size: 32px; }
  .ad--square .mark-x { left: 156px; top: 177px; font-size: 11px; }
  .ad--square .live-tag { left: 204px; top: 199px; width: 52px; height: 16px; font-size: 11px; }
  .ad--square .news-band--red { left: 40px; top: 218px; width: 212px; height: 43px; }
  .ad--square .news-band--red .news-band__word { font-size: 32px; }
  .ad--square .news-band--blue { left: 33px; top: 264px; width: 135px; height: 40px; }
  .ad--square .news-band--blue .news-band__word { font-size: 32px; }
  .ad--square .headline-finally { left: 266px; top: 255px; font-size: 45px; }
  .ad--square .subhead { left: 31px; top: 318px; font-size: 16px; }
  .ad--square .aside-fun { left: 309px; top: 343px; font-size: 18px; }
  .ad--square .cta { left: 31px; top: 376px; width: 98px; height: 28px; font-size: 13px; }
  .ad--square .site-url { left: 170px; top: 392px; }
  .ad--square .dot-grid { left: 381px; top: 385px; }

  /* wide ad placement */
  .ad--wide .offer-badge { left: 48px; top: 43px; width: 59px; height: 46px; border-radius: 20px; }
  .ad--wide .offer-badge__small { font-size: 10px; }
  .ad--wide .offer-badge__big { font-size: 19px; }
  .ad--wide .live-tag { left: 236px; top: 86px; width: 65px; height: 22px; font-size: 15px; }
  .ad--wide .mark-x { left: 314px; top: 148px; font-size: 13px; }
  .ad--wide .news-band--red { left: 40px; top: 111px; width: 255px; height: 54px; }
  .ad--wide .news-band--red .news-band__word { font-size: 40px; }
  .ad--wide .news-band--blue { left: 30px; top: 167px; width: 166px; height: 50px; }
  .ad--wide .news-band--blue .news-band__word { font-size: 40px; }
  .ad--wide .headline-finally { left: 208px; top: 180px; font-size: 44px; }
  .ad--wide .subhead { left: 45px; top: 233px; font-size: 20px; }
  .ad--wide .cta { left: 48px; top: 313px; width: 110px; height: 31px; font-size: 14px; }
  .ad--wide .aside-fun { left: 277px; top: 312px; font-size: 31px; }
</style>
</head>
<body>
<main class="canvas">

  <!-- Square ad -->
  <section class="ad ad--square">
    <svg class="ad__art" viewBox="0 0 438 438" aria-hidden="false">
      <defs>
        <linearGradient id="photoSquare" x1="0" y1="0" x2="1" y2="1">
          <stop offset="0" stop-color="var(--photo-a)"/>
          <stop offset="0.55" stop-color="var(--photo-b)"/>
          <stop offset="1" stop-color="var(--photo-c)"/>
        </linearGradient>
      </defs>
      <polygon role="img" aria-label="Photo of a woman doing a dumbbell row in a busy gym class" points="112,0 418,0 438,43 438,218 222,218" fill="url(#photoSquare)"/>
      <polygon class="stripe-white" points="88,0 98,0 168,134 159,134" fill="var(--white)"/>
      <polygon class="stripe-yellow" points="100,0 112,0 200,172 189,172" fill="var(--yellow)"/>
    </svg>

    <div class="offer-badge">
      <span class="offer-badge__small">GET</span>
      <span class="offer-badge__big">50%</span>
      <span class="offer-badge__small">OFF</span>
    </div>
    <span class="mark-x">✕</span>
    <div class="live-tag">LIVE <span class="live-tag__dot"></span></div>
    <div class="news-band news-band--red"><span class="news-band__word">BREAKING</span></div>
    <div class="news-band news-band--blue"><span class="news-band__word">NEWS</span></div>
    <h1 class="headline-finally">FINALLY!</h1>
    <p class="subhead">Brackenford Gets the Gym<br>That Actually Delivers Results</p>
    <span class="aside-fun">(AND IT'S FUN!)</span>
    <div class="cta">FREE TRIAL</div>
    <span class="site-url">www.brackenfordfit.com</span>
    <div class="dot-grid"><span></span><span></span><span></span><span></span><span></span><span></span></div>
  </section>

  <!-- Wide ad -->
  <section class="ad ad--wide">
    <svg class="ad__art" viewBox="0 0 690 361" aria-hidden="false">
      <defs>
        <linearGradient id="photoWide" x1="0" y1="0" x2="1" y2="1">
          <stop offset="0" stop-color="var(--photo-a)"/>
          <stop offset="0.55" stop-color="var(--photo-b)"/>
          <stop offset="1" stop-color="var(--photo-c)"/>
        </linearGradient>
      </defs>
      <polygon role="img" aria-label="Photo of a woman doing a dumbbell row in a busy gym class" points="304,0 690,0 690,361 500,361 455,285" fill="url(#photoWide)"/>
      <polygon class="stripe-white" points="276,0 287,0 373,162 362,166" fill="var(--white)"/>
      <polygon class="stripe-yellow" points="290,0 304,0 414,213 402,218" fill="var(--yellow)"/>
    </svg>

    <div class="offer-badge">
      <span class="offer-badge__small">GET</span>
      <span class="offer-badge__big">50%</span>
      <span class="offer-badge__small">OFF</span>
    </div>
    <div class="live-tag">LIVE <span class="live-tag__dot"></span></div>
    <span class="mark-x">✕</span>
    <div class="news-band news-band--red"><span class="news-band__word">BREAKING</span></div>
    <div class="news-band news-band--blue"><span class="news-band__word">NEWS</span></div>
    <h2 class="headline-finally">FINALLY!</h2>
    <p class="subhead">Brackenford Gets the Gym<br>That Actually Delivers Results</p>
    <div class="cta">FREE TRIAL</div>
    <span class="aside-fun">(AND IT'S FUN!)</span>
  </section>

</main>
</body>
</html>
```